KVR Biz Cards

We are a property management company that manages luxury level residential estates. As such, we need a business card design that gives a high end feel. The idea at the moment is to list the services offered on the back of the card, and our company information on the front of the card.

Services for the back of the card are as follows:
Professional Property Management service, Home Hosting & Concierge Service, Holliday Home / Income Property Management

```html
<!DOCTYPE html>
<html lang="en">
<head>
<meta charset="utf-8">
<title>KVR Biz Cards</title>
<link rel="stylesheet" href="https://fonts.googleapis.com/css2?family=Montserrat:wght@500;600;700&display=swap">
<style>
  :root {
    --backdrop: #e3ebb6;
    --card: #050505;
    --gold: #e9c84a;
    --gold-deep: #c99a1e;
    --gold-light: #fbe88a;
    --ink: #ffffff;
  }
  * { box-sizing: border-box; margin: 0; padding: 0; }
  html, body {
    width: 960px;
    height: 1200px;
    overflow: hidden;
    background: var(--backdrop);
    font-family: "Montserrat", Arial, sans-serif;
  }
  .canvas {
    position: relative;
    width: 960px;
    height: 1200px;
  }
  .card {
    position: absolute;
    left: 167px;
    width: 646px;
    height: 370px;
    background: var(--card);
    box-shadow: 0 18px 30px rgba(40, 50, 10, 0.35);
    overflow: hidden;
  }
  .card--front { top: 203px; }
  .card--back { top: 626px; }
  .card__frame {
    position: absolute;
    inset: 0;
    width: 646px;
    height: 370px;
  }
  .card__frame polyline {
    fill: none;
    stroke: url(#goldStroke);
    stroke-width: 3.5;
  }

  /* Brand name */
  .brand {
    position: absolute;
    display: flex;
    align-items: center;
    gap: 10px;
    color: var(--gold);
    font-weight: 600;
    letter-spacing: 1px;
    line-height: 1;
  }
  .brand__square {
    width: 14px;
    height: 14px;
    background: var(--gold);
  }
  .card--front .brand {
    left: 50%;
    top: 164px;
    transform: translateX(-50%);
    font-size: 46px;
  }
  .card--back .brand {
    left: 100px;
    top: 192px;
    font-size: 40px;
  }

  /* Front text */
  .company {
    position: absolute;
    left: 0;
    right: 0;
    top: 226px;
    text-align: center;
    color: var(--ink);
    font-size: 30px;
    font-weight: 600;
    letter-spacing: 0.6px;
  }
  .tagline {
    position: absolute;
    left: 0;
    right: 0;
    top: 261px;
    text-align: center;
    color: var(--ink);
    font-size: 15px;
    font-weight: 500;
    letter-spacing: 0.5px;
  }

  /* Back services */
  .services {
    position: absolute;
    left: 302px;
    top: 89px;
    list-style: none;
  }
  .services__item {
    position: relative;
    padding-left: 35px;
    margin-bottom: 25px;
    color: var(--ink);
    font-size: 17px;
    font-weight: 600;
    line-height: 24px;
  }
  .services__item::before {
    content: "";
    position: absolute;
    left: 0;
    top: 6px;
    width: 12px;
    height: 11px;
    background: linear-gradient(90deg, var(--gold-deep), var(--gold-light));
  }
</style>
</head>
<body>
<svg width="0" height="0" style="position:absolute">
  <defs>
    <linearGradient id="goldStroke" x1="0" y1="0" x2="1" y2="1">
      <stop offset="0" stop-color="#c99a1e"/>
      <stop offset="0.45" stop-color="#fbe88a"/>
      <stop offset="1" stop-color="#d9ad2c"/>
    </linearGradient>
  </defs>
</svg>

<main class="canvas">
  <section class="card card--front" aria-label="Front of business card">
    <svg class="card__frame" viewBox="0 0 646 370" aria-hidden="true">
      <polyline points="24,351 24,22 623,22 623,351 68,351"/>
    </svg>
    <div class="brand"><span>KVR</span><span class="brand__square"></span></div>
    <h1 class="company">KAVREN MANAGEMENT</h1>
    <p class="tagline">Designed to Bring You Total Comfort</p>
  </section>

  <section class="card card--back" aria-label="Back of business card">
    <svg class="card__frame" viewBox="0 0 646 370" aria-hidden="true">
      <polyline points="24,351 24,22 623,22 623,351 68,351"/>
    </svg>
    <div class="brand"><span>KVR</span><span class="brand__square"></span></div>
    <ul class="services">
      <li class="services__item">Professional Property<br>Management service</li>
      <li class="services__item">Home Hosting &amp;<br>Concierge Service</li>
      <li class="services__item">Holliday Home / Income<br>Property Management</li>
    </ul>
  </section>
</main>
</body>
</html>
```